Brochure and Banner Designs

We need to put the attached brochure in a very professional, intriguing and relaxing to read and interest follow up...we would like to work with the colours of our logo...the brown stands for healthy homes, the blue for engaged communities and the green for natural surroundings. We bought the pic in the brochure. We would like to see the kid with the puff in a transparent background to minimize distraction. Also we would like the picture to blend beautifully with the background. We have used a template with an idea if what we are looking for.

We also need a banner design. I have attached the idea as well. I also attached the logo of the company so you can play with ideas around it. The 3d pic is not final, we will receive it next week, for now lets leave the space for it and work on the look and the information...we thought about add the colours that belong to each pillar as indicated in the paragraph above. It could be kind of abstract...blending each colour in the transition...Please note that I included a closer pic of the buildings, since it could be blended with the aerial view. As indicated before the aerial view is draft for now.

Any way good lock and I will asssit all your questions....

Lucia
Updates

Please note that for the banner, we were advised that people will only have 3 seconds to see it (sicne they will be driving)...so to simplify the message, it was suggested removing the description under each pillar...so lets only leave:

Maison saines
Collectivité bienveillante
Cadre de vie naturel

Thanks,
Lucia

Please when write L'Étang on the top of the banner, please ensure is written as the file I just attached to the fiel for your information.

Hi, everyone...

                                 

Thanks for your time and ideas!

Lucia

Hi, Guys

Could you please confirm who is planning to submit designs..?

Thanks,

Lucia

I hope to receive more designs...

Lucia

                                       

1058924 Preferred front cover (only comment too beige) and center as for the family suggested the building behind the family and replaced the kids by the family in this design.

The vision and mission exchange position with the Do you know…for this page suggested removing the kid with the puff and using the asthma kid as a backgrounder as it is done in design 1066529 but only covering this page and making the asthma puff more evident. This will provide more space for text in that page. The vision and mission as design 1066529.

Proactive Approach on center inside line to be removed…so on the top of this page Healthy Homes..pics are preferred squared..

The engaged community pic has been change for the grandpa with kids around. Attached in the file.

As for the banner, it is considered too blue…please follow the background use for brochure cover for design 1058924. As for the website only use quorvane.com do not write quorvane twice. Pleas edo not use bullets for the elements…

Thanks for your participation!

Lucia

                                   

the tree as a background is vey nice...

Target Market(s)

Highly educated people specially women 35-55 years old $70K plus salaries

Industry/Entity Type

It Company

Requirements
Must have
• The logo
All the info included in the attachements...ideas are welcome on the language, structure, flow, colours, etc...
Nice to have
• Nice flow...focus points.
Should not have
• non earth colours

```html
<!DOCTYPE html>
<html lang="en">
<head>
<meta charset="utf-8">
<title>quorvane – Healthy Living Communities brochure</title>
<link rel="stylesheet" href="https://fonts.googleapis.com/css2?family=Carlito:ital,wght@0,400;0,700;1,400&family=Arimo:wght@400;700&display=swap">
<style>
  :root {
    --backdrop: #e4e4e2;
    --green-light: #cfe3b6;
    --green-mid: #8cc07a;
    --green-deep: #4f9a4c;
    --green-dark: #2f7a3a;
    --khaki: #d8d29a;
    --khaki-light: #eeeac8;
    --brown: #8a5a1e;
    --gold: #8a6a12;
    --yellow: #f2e56c;
    --amber: #b8661c;
    --ink: #3e3220;
    --white: #ffffff;
  }
  * { box-sizing: border-box; margin: 0; padding: 0; }
  html, body { width: 1200px; height: 900px; overflow: hidden; }
  body { background: var(--backdrop); font-family: "Arimo", Arial, sans-serif; color: var(--ink); position: relative; }

  .sheet { position: absolute; display: flex; overflow: hidden; }

  /* Outside */
  .sheet--outside { left: 17px; top: 10px; width: 570px; height: 440px;
    background: linear-gradient(180deg, var(--green-light), var(--green-mid) 60%, #a9d08f); }
  .sheet__waves { position: absolute; inset: 0; pointer-events: none; }
  .panel { position: relative; width: 190px; height: 100%; z-index: 1; }
  .panel + .panel { border-left: 1px solid rgba(255,255,255,.45); }

  .mission { padding: 30px 18px 0; text-align: center;
    background: linear-gradient(180deg, rgba(236,244,220,.8), rgba(180,214,150,.4)); }
  .mission__title { font-family: "Carlito", Calibri, sans-serif; font-weight: 400; font-size: 19px; color: var(--brown); margin-bottom: 26px; }
  .mission__text { font-size: 10.4px; line-height: 1.25; margin-bottom: 15px; }

  .contact { background: linear-gradient(180deg, #5fa857, var(--green-deep) 55%, #62a85a); text-align: center; color: var(--white); padding-top: 120px; }
  .brand { display: flex; align-items: center; justify-content: center; gap: 8px; }
  .brand__dot { width: 16px; height: 16px; border-radius: 50%; background: var(--yellow); }
  .brand__name { font-family: "Carlito", Calibri, sans-serif; font-weight: 700; font-size: 36px; color: var(--yellow); line-height: 1; }
  .brand__tagline { font-family: "Carlito", Calibri, sans-serif; font-size: 12.5px; color: #f3f6cf; margin: 4px 0 22px; }
  .contact__address { font-size: 11px; line-height: 1.3; font-style: normal; }
  .contact__web { font-family: "Carlito", Calibri, sans-serif; font-size: 16px; color: #f6f3c4; margin-top: 30px; }

  .cover { text-align: center; }
  .cover__photo { position: absolute; left: 4px; top: 40px; width: 180px; height: 130px; border-radius: 50%;
    background: radial-gradient(ellipse at center, #f4efe4 30%, #d8e6c4 60%, rgba(200,222,170,0) 72%); }
  .cover__title { position: absolute; left: 0; right: 0; top: 252px; font-family: "Carlito", Calibri, sans-serif;
    font-size: 22px; line-height: 1.18; color: var(--gold); }

  /* Inside */
  .sheet--inside { left: 608px; top: 426px; width: 576px; height: 440px;
    background: var(--green-dark); padding: 6px 0 6px; gap: 2px; }
  .page { position: relative; flex: 1; height: 100%;
    background: linear-gradient(180deg, #c9d79a, #dde2b0 40%, #b9d28e); font-size: 7.8px; line-height: 1.2; }
  .page:nth-child(2), .page:nth-child(3) { background: linear-gradient(180deg, #a9d08c, #c7deac 45%, #94c47a); }
  .page__head { height: 40px; display: flex; align-items: center; justify-content: center; text-align: center;
    background: linear-gradient(180deg, #6ea85a, #8fbc6e); font-family: "Carlito", Calibri, sans-serif;
    color: var(--yellow); font-size: 17px; line-height: 1.05; }
  .page:nth-child(1) .page__head { background: linear-gradient(180deg, #9eab5c, #b7b977); }
  .page__body { padding: 6px 8px 0; }
  .page p { margin-bottom: 7px; }
  .subhead { font-family: "Carlito", Calibri, sans-serif; font-style: italic; font-size: 12.5px; color: var(--amber); margin: 4px 0 8px; }

  .facts { position: absolute; left: 6px; right: 6px; top: 44px; bottom: 4px; padding: 6px 6px;
    background: linear-gradient(180deg, var(--khaki-light), var(--khaki)); box-shadow: inset 0 0 6px rgba(120,110,50,.35); }
  .photo { display: block; margin: 6px auto 10px; }
  .photo--inhaler { width: 104px; height: 82px; background: linear-gradient(135deg, #f1d9c4, #cfe1ee 60%, #e8e4d6); }
  .photo--house { width: 132px; height: 88px; background: linear-gradient(180deg, #8cb06a, #d9c68a 45%, #4f7a34); }
  .photo--reading { width: 116px; height: 80px; background: linear-gradient(135deg, #8a6a4a, #d7c2a6 50%, #b13c38); }
  .photo--aerial { width: 116px; height: 72px; background: linear-gradient(135deg, #3f6a32, #6f9550 50%, #9fa48c); }
  .center { text-align: center; }
  .web-link { font-size: 10px; color: var(--white); }
</style>
</head>
<body>

<section class="sheet sheet--outside" aria-label="Brochure outside">
  <svg class="sheet__waves" viewBox="0 0 570 440" preserveAspectRatio="none" aria-hidden="true">
    <path d="M0 340 C150 300 320 420 570 330 L570 440 L0 440 Z" fill="#b7d99a" opacity=".45"/>
    <path d="M0 370 C170 340 360 430 570 380" fill="none" stroke="#e8f2cf" stroke-width="1.5" opacity=".7"/>
    <path d="M380 200 C430 150 520 180 570 230" fill="none" stroke="#e8f2cf" stroke-width="1.2" opacity=".6"/>
  </svg>

  <article class="panel mission">
    <h2 class="mission__title">Our Mission</h2>
    <p class="mission__text">To develop healthy residential communities that infuse life with vitality by nurturing the mind, body and soul.</p>
    <p class="mission__text">Behind this mission is a desire to address the unprecedented challenges of our times.</p>
    <p class="mission__text">Our deep conviction to effecting real change, our collective understanding of the paramount role of relationships to health, and our complementary experience in business, technical, and large scale infrastructure capacities, have been instrumental in creating what we trust is a truly inspiring and empowering model of healthy living communities.</p>
  </article>

  <article class="panel contact">
    <div class="brand">
      <span class="brand__dot"></span>
      <span class="brand__name">quorvane</span>
    </div>
    <p class="brand__tagline">Healthy, Living Communities</p>
    <address class="contact__address">
      4820 Rue Lavallée<br>
      PO 63715 Belcourt<br>
      Rivermont&nbsp; QC<br>
      K2X 5P4<br>
      613-555-0187<br>
      info@quorvane.com
    </address>
    <p class="contact__web">www.quorvane.com</p>
  </article>

  <article class="panel cover">
    <div class="cover__photo" role="img" aria-label="Photo of a multigenerational family sitting together"></div>
    <h1 class="cover__title">Healthy<br>Living<br>Communities</h1>
  </article>
</section>

<section class="sheet sheet--inside" aria-label="Brochure inside">
  <article class="page">
    <h2 class="page__head">Do You Know...</h2>
    <div class="facts">
      <p>The Global Wellness Council (GWC) states health is 'A state of complete physical, mental, and social wellbeing, and not merely the absence of disease or infirmity.</p>
      <p>The word 'health' is derived from the Greek word 'hal' or whole. Therefore health has a holistic perspective.</p>
      <div class="photo photo--inhaler" role="img" aria-label="Photo of a young child using an asthma inhaler mask"></div>
      <p>According to the Continental Institute of Respiratory Health, 50% of all illnesses are either caused or aggravated by poor indoor air quality.</p>
      <p>61% of Canada's fresh water is rated fair, marginal or poor due to physical, microbiological, chemical, and/or radiological contaminants.</p>
      <p>Many researchers believe that interpersonal relationships are the most crucial factor to overall health.</p>
      <p>A growing body of scientific evidence indicates that being with or even looking at nature – particularly in its wild state - produces positive physical, mental, social and spiritual benefits.</p>
    </div>
  </article>

  <article class="page">
    <h2 class="page__head">A Proactive &amp;<br>Holistic Approach</h2>
    <div class="page__body">
      <h3 class="subhead">Healthy Homes</h3>
      <p>Low contaminant materials for people suffering diverse hypersensitivities. Hospital grade air filtration.</p>
      <p>Clean water (piping and filtration National Water Standards Board (NWSB) certified).</p>
      <div class="photo photo--house" role="img" aria-label="Photo of a house surrounded by trees and lawn"></div>
      <h3 class="subhead">Natural Surroundings</h3>
      <p>10.3 acres of prolific natural beauty.</p>
      <p>Low impact designs and materials.</p>
      <p>Natural resources conservation (30% water and 60% energy).</p>
    </div>
  </article>

  <article class="page">
    <h2 class="page__head">Engaged Communities</h2>
    <div class="page__body">
      <p>Community living in nature.</p>
      <p>Multigenerational indoors and outdoors recreational and leisure facilities (Common room, exterior patio, gym, yoga room, workshop, indoor playroom).</p>
      <div class="photo photo--reading" role="img" aria-label="Photo of a grandfather reading a book with children"></div>
      <p class="center">Community engagement facilitation.</p>
      <p class="center">To learn more, you could visit our website at:<br><span class="web-link">www.quorvane.com</span></p>
      <div class="photo photo--aerial" role="img" aria-label="Aerial view of the wooded community site"></div>
    </div>
  </article>
</section>

</body>
</html>
```